ZAMO needs a beautiful/corp web page

We are a pump an compressor repair facility in Alberta Canada. We love clean looks. white yellows greens blues. main page should involve conola fields, sun shine

Reason: i will be guaranteeing the project keep up the good work

Requirements
Must have
• open conola fields

```html
<!DOCTYPE html>
<html lang="en">
<head>
<meta charset="utf-8">
<title>ZAMO Rotating Solutions</title>
<link href="https://fonts.googleapis.com/css2?family=Lato:wght@400;700&family=Oswald:wght@400&display=swap" rel="stylesheet">
<style>
:root{
  --page:#e6e7e8;
  --orange:#f4a300;
  --ink:#231f20;
  --dark:#2b2624;
  --white:#ffffff;
  --green:#2f7a3a;
  --line:#c9c9c9;
  --hero-top:#8dbde6;
  --hero-bottom:#6aa548;
}
*{box-sizing:border-box;margin:0;padding:0}
html,body{width:1200px;height:857px;overflow:hidden}
body{background:var(--page);font-family:'Lato',sans-serif;color:var(--ink);position:relative;border-top:2px solid var(--orange)}
.phone-tab{position:absolute;left:734px;top:0;width:203px;height:26px;background:var(--orange);border-radius:0 0 8px 8px;color:var(--white);font-size:16px;font-weight:700;display:flex;align-items:center;padding-left:16px;gap:8px}
.phone-tab svg{flex:none}
.brand{position:absolute;left:264px;top:80px;display:flex;align-items:center;gap:8px}
.brand-dot{width:14px;height:14px;border-radius:50%;background:var(--orange)}
.brand-name{font-size:34px;font-weight:700;color:var(--ink);letter-spacing:1px;line-height:1}
.search{position:absolute;left:720px;top:92px;width:216px;height:20px;display:flex}
.search-field{flex:1;background:var(--white);border:1px solid var(--line);font-size:10px;color:#9a9a9a;padding:4px 8px;line-height:11px}
.search-btn{width:44px;background:var(--orange);display:flex;align-items:center;justify-content:center}
.main-nav{position:absolute;left:250px;top:126px;width:700px;height:26px;display:flex;background:var(--white);border:1px solid #f0c060}
.main-nav a{flex:1;text-align:center;font-size:12px;line-height:24px;color:var(--ink);text-decoration:none;border-left:1px solid #f0c060}
.main-nav a:first-child{border-left:none}
.main-nav a.active{background:var(--orange);color:var(--white)}
.hero{position:absolute;left:250px;top:152px;width:700px;height:238px;overflow:hidden}
.hero-image{position:absolute;inset:0;background:linear-gradient(180deg,var(--hero-top) 0%,var(--hero-bottom) 100%)}
.hero-btn{position:absolute;top:110px;height:16px;background:var(--green);color:var(--white);font-size:10px;line-height:16px;padding:0 4px}
.hero-btn.back{left:0}
.hero-btn.next{right:0}
.hero-caption{position:absolute;left:14px;top:193px;color:var(--white)}
.hero-caption h2{font-size:14.5px;font-weight:400;line-height:18px}
.hero-caption p{font-size:9.5px;line-height:12px;margin-top:1px}
.content{position:absolute;left:250px;top:400px;width:700px;height:242px;background:var(--white)}
.welcome{position:absolute;left:12px;top:24px;width:432px}
.welcome h1{font-size:17.6px;font-weight:700;line-height:20px;color:var(--ink)}
.welcome h1 span{color:var(--orange);font-weight:400}
.welcome p{font-size:9.2px;line-height:15.2px;margin-top:9px;padding-left:2px}
.welcome p + p{margin-top:15px}
.quote{position:absolute;left:703px;top:421px;width:232px;height:186px;background:var(--orange);border-radius:8px;font-family:'Oswald',sans-serif;color:var(--white)}
.quote h3{font-size:22px;font-weight:400;position:absolute;left:15px;top:9px;line-height:28px}
.quote label{position:absolute;font-size:10.4px;line-height:12px}
.quote .field{position:absolute;background:var(--white);border:1px solid #d98f00;height:16px;width:97px}
.quote .field.msg{width:161px;height:39px}
.quote-btn{position:absolute;left:720px;top:591px;width:199px;height:29px;background:var(--ink);border-radius:8px;color:var(--white);font-family:'Oswald',sans-serif;font-size:15px;line-height:29px;text-align:center}
.footer{position:absolute;left:250px;top:642px;width:700px;height:159px;background:var(--dark);color:var(--white)}
.footer-col{position:absolute;top:17px}
.footer-col h4{font-size:16px;font-weight:400;line-height:20px}
.footer-col h5{font-size:10.6px;font-weight:400;line-height:12px}
.footer-col p,.footer-col li{font-size:9.2px;line-height:12px}
.footer-col ul{list-style:none;margin-top:10px}
.footer-col li{margin-bottom:7.2px}
.col-about{left:14px;width:205px}
.col-about p{margin-top:4px}
.col-group{left:251px}
.col-contact{left:476px;width:210px}
.col-contact p{margin-top:12px}
.col-contact p + p{margin-top:12px}
.footer-divider{position:absolute;left:237px;top:16px;width:1px;height:128px;background:#9a9390}
.copyright{position:absolute;left:257px;top:806px;font-size:9.2px;color:var(--ink)}
</style>
</head>
<body>
<div class="phone-tab">
  <svg width="16" height="16" viewBox="0 0 16 16" aria-hidden="true"><circle cx="8" cy="8" r="8" fill="#fff"/><path d="M5 4.5c.6-.4 1.1-.3 1.4.2l.7 1.2c.2.4.1.8-.3 1.1l-.5.4c.4.9 1.1 1.6 2 2l.4-.5c.3-.4.7-.5 1.1-.3l1.2.7c.5.3.6.8.2 1.4-.5.7-1.3 1-2.1.7C7 10.7 5.3 9 4.6 7c-.3-.8 0-1.8.4-2.5z" fill="#f4a300"/></svg>
  +00 (0) 0000 000 000
</div>

<div class="brand">
  <span class="brand-dot"></span>
  <span class="brand-name">ZAMO</span>
</div>

<div class="search">
  <div class="search-field">SEARCH</div>
  <div class="search-btn">
    <svg width="11" height="11" viewBox="0 0 12 12" aria-hidden="true"><circle cx="5" cy="5" r="3.5" fill="none" stroke="#fff" stroke-width="1.8"/><path d="M7.6 7.6L10.8 10.8" stroke="#fff" stroke-width="2" stroke-linecap="round"/></svg>
  </div>
</div>

<nav class="main-nav">
  <a class="active" href="#">HOME</a>
  <a href="#">ABOUT US</a>
  <a href="#">TESTING</a>
  <a href="#">OUR SERVICES</a>
  <a href="#">USED EQUIPMENT</a>
  <a href="#">CONTACT US</a>
</nav>

<section class="hero">
  <div class="hero-image" role="img" aria-label="Banner photo: sunlit green canola fields under a blue sky"></div>
  <div class="hero-btn back">BACK</div>
  <div class="hero-btn next">NEXT</div>
  <div class="hero-caption">
    <h2>WELCOME TO ZAMO ROTATING SOLUTIONS</h2>
    <p>LOREM IPSUM IS SIMPLY DUMMY TEXT OF THE PRINTING AND TYPESETTING INDUSTRY.</p>
  </div>
</section>

<main class="content">
  <div class="welcome">
    <h1><span>WELCOME TO</span> ZAMO ROTATING SOLUTIONS</h1>
    <p>Lorem Ipsum is simply dummy text of the printing and typesetting industry. Lorem Ipsum has been the industry's standard dummy text ever since the 1500s, when an unknown printer took a galley of type and scrambled it to make a type specimen book. It has survived not only five centuries, but also the leap into electronic typesetting, remaining essentially unchanged. It was popularised in the 1960s with the release of Lettrafix sheets containing Lorem Ipsum passages, and more recently with desktop publishing software like Pagecraft Studio including versions of Lorem Ipsum.</p>
    <p>Lorem Ipsum is simply dummy text of the printing and typesetting industry. Lorem Ipsum has been the industry's standard dummy text ever since the 1500s.</p>
  </div>
</main>

<form class="quote">
  <h3>ONLINE QUOTE FORM</h3>
  <label style="left:15px;top:47px">FIRST NAME</label>
  <label style="left:119px;top:47px">LAST NAME</label>
  <div class="field" style="left:15px;top:60px"></div>
  <div class="field" style="left:119px;top:60px"></div>
  <label style="left:15px;top:84px">EMAIL ADDRESS</label>
  <label style="left:119px;top:84px">PHONE NUMBER</label>
  <div class="field" style="left:15px;top:97px"></div>
  <div class="field" style="left:119px;top:97px"></div>
  <label style="left:15px;top:119px">MESSAGE</label>
  <div class="field msg" style="left:55px;top:118px"></div>
</form>
<div class="quote-btn">GET A FREE QUOTE</div>

<footer class="footer">
  <div class="footer-col col-about">
    <h4>ABOUT</h4>
    <h5>ZAMO ROTATION SOLUTIONS</h5>
    <p>Lorem Ipsum is simply dummy text of the printing and typesetting industry. Lorem Ipsum has been the industry's standard dummy text ever since the 1500s, when an unknown printer took a galley of type and scrambled it to make a type specimen book.</p>
  </div>
  <div class="footer-divider"></div>
  <div class="footer-col col-group">
    <h4>GROUP COMPANIES</h4>
    <ul>
      <li>-Lorem Ipsum</li>
      <li>-Lorem Ipsum</li>
      <li>-Lorem Ipsum</li>
      <li>-Lorem Ipsum</li>
    </ul>
  </div>
  <div class="footer-col col-contact">
    <h4>CONTACT US</h4>
    <p>Lorem Ipsum is simply dummy text of the printing and typesetting industry.</p>
    <p>Tel: +00 (0) 0000 000 000<br>Fax: +00 (0) 0000 000 000</p>
    <p>Email: sales@zamorotatingsolutions.com</p>
  </div>
</footer>

<div class="copyright">Copyright © 2013 ZAMO Rotating Solutions. All Rights Reserved.</div>
</body>
</html>
```